A Must Standout Business Card Design

I need A card that stands out from the rest. Possibly raised letters or Metallic card, Shiny or glossy, Looking for a more modern look or something throwback design would be nice. So i'm a open to different designs. I have a logo but not to happy with it. I will send it on a sample business card I do like.I might like you to tweak the designed card I am sending you. A new logo may be in order too. Make logo something that can be engraved on metal. I was thinking possibly KR in a box or KR mirror image or Backward E then a forward B in a circle. The name of my company is KR Works Inc. I designed an innovative hand tool to remove Valve Cores. I call the tool the Stem Pin Clasp. My tool grips and holds onto valve cores like no other tool does. Check it out at my website stempinclasp.com Maybe put a picture of the tool on the card raised or embossed or that spot gloss.
Updates
Everybody I must say have sent over some awesome designs! Every submission has been my favorite so I will be making my decision after the deadline. Nice work everyone!
Target Market(s)
Automotive people, People who wholesale refrigeration parts and equipment, People who use tools
Industry/Entity Type
Business
Contact Information for Business Card
KR Works Inc., 4172 Larkfield Rd. Unit C Morris IL 60450, Doug Whitlow President, 708-555-0193, Stempinclasp.com, Logo
Look and feel
Each slider illustrates characteristics of the customer's brand and the style your logo design should communicate.

```html
<!DOCTYPE html>
<html lang="en">
<head>
<meta charset="utf-8">
<title>KR Works Inc. – Business Card</title>
<link href="https://fonts.googleapis.com/css2?family=PT+Sans:wght@700&display=swap" rel="stylesheet">
<style>
  :root {
    --page-bg: #f4f4f5;
    --card-edge: #4a4d7e;
    --card-mid: #8f90bb;
    --card-glow: #f3f3fa;
    --ink: #2e3436;
    --brand-grey: #6d7174;
    --tool-light: #b9bcbe;
    --tool-dark: #7c8083;
  }
  * { margin: 0; padding: 0; box-sizing: border-box; }
  html, body {
    width: 1200px;
    height: 1009px;
    overflow: hidden;
    background: var(--page-bg);
    font-family: "PT Sans", "Arial Narrow", sans-serif;
    font-weight: 700;
  }
  .business-card {
    position: absolute;
    left: 100px;
    top: 234px;
    width: 1000px;
    height: 540px;
    border-radius: 38px;
    overflow: hidden;
    background: radial-gradient(ellipse 62% 75% at 50% 47%, var(--card-glow) 0%, var(--card-mid) 58%, var(--card-edge) 100%);
  }
  .brand {
    position: absolute;
    left: 50px;
    top: 344px;
    display: flex;
    align-items: center;
    gap: 10px;
    color: var(--brand-grey);
    font-size: 32px;
    line-height: 1;
    white-space: nowrap;
  }
  .brand-square {
    width: 22px;
    height: 22px;
    background: var(--brand-grey);
  }
  .tool-art {
    position: absolute;
    left: 322px;
    top: 48px;
    width: 96px;
    height: 457px;
    border-radius: 48px 48px 10px 10px;
    background: linear-gradient(90deg, var(--tool-dark), var(--tool-light) 50%, var(--tool-dark));
  }
  .holder {
    position: absolute;
    right: 67px;
    top: 64px;
    text-align: right;
    color: var(--ink);
  }
  .holder-name { font-size: 36px; line-height: 1.1; }
  .holder-title { font-size: 23px; line-height: 1.2; }
  .rule {
    position: absolute;
    left: 487px;
    right: 67px;
    top: 153px;
    height: 3px;
    background: var(--ink);
  }
  .contact {
    position: absolute;
    right: 67px;
    top: 318px;
    text-align: right;
    color: var(--ink);
    font-size: 25px;
    line-height: 36px;
    font-style: normal;
  }
</style>
</head>
<body>
  <div class="business-card">
    <div class="brand">
      <span class="brand-square"></span>
      <span class="brand-name">KR Works Inc.</span>
    </div>
    <div class="tool-art" role="img" aria-label="Embossed metallic image of the Stem Pin Clasp hand tool with key ring"></div>
    <div class="holder">
      <div class="holder-name">Doug Whitlow</div>
      <div class="holder-title">President</div>
    </div>
    <div class="rule"></div>
    <address class="contact">
      4172 Larkfield Rd<br>
      Unit C Halbrook<br>
      OH, 45017 USA<br>
      Tel: (708) 555-0193<br>
      www.Stempinclasp.com
    </address>
  </div>
</body>
</html>
```